Hvac and insulation company needs good looking business card design

We are hvac and insulation company and looking for a new business cards that look to today standards designs

Target Market(s)

homeowners

Industry/Entity Type

Hvac

Contact Information for Business Card

Name: Walter Brindley
Home comfort consultant
address: 4827 Moravia Ct #215 Oakland, CA 94602
office: 888-731-5096
cell: 510-842-3917
Lic.# 583164
Email: walter@corvane-hvac.example
Web: corvane-hvac.example

Requirements
Must have
• clean and sleek look
Nice to have
• simple with a clean look
Should not have
• to busy business card

```html
<!DOCTYPE html>
<html lang="en">
<head>
<meta charset="utf-8">
<title>Corvane — Business Card</title>
<link rel="stylesheet" href="https://fonts.googleapis.com/css2?family=Montserrat:ital,wght@0,300;0,400;0,700;1,300&display=swap">
<style>
  :root {
    --orange: #f47f20;
    --orange-deep: #f15a24;
    --orange-mid: #f7941d;
    --yellow: #fdc614;
    --ink: #4d4d4f;
    --paper: #ffffff;
    --canvas: #ffffff;
  }
  * { margin: 0; padding: 0; box-sizing: border-box; }
  html, body {
    width: 1200px; height: 1200px; overflow: hidden;
    background: var(--canvas);
  }
  .sheet { position: relative; width: 1200px; height: 1200px; }

  .card {
    position: absolute;
    width: 653px; height: 423px;
    background: var(--paper);
    box-shadow: 6px 8px 22px rgba(0,0,0,0.12);
    overflow: hidden;
  }
  .card--front {
    left: 278px; top: 146px;
    background: linear-gradient(90deg, var(--yellow) 0%, var(--orange-mid) 45%, var(--orange-deep) 100%);
  }
  .card--back { left: 280px; top: 620px; }

  .front-panel {
    position: absolute; left: 0; right: 0; top: 84px; height: 258px;
    background: var(--paper);
    display: flex; align-items: center; justify-content: center; gap: 22px;
  }
  .brand-dot {
    width: 52px; height: 52px; border-radius: 50%;
    background: var(--orange); flex: none;
  }
  .brand-name {
    font-family: "Montserrat", sans-serif;
    font-weight: 400; font-size: 76px; line-height: 1;
    color: var(--orange); letter-spacing: -1px;
  }

  .contact { position: absolute; left: 52px; font-family: "Montserrat", sans-serif; color: var(--ink); line-height: 1; white-space: nowrap; }
  .contact__name { top: 54px; font-size: 30px; font-weight: 700; color: var(--orange); letter-spacing: 0.3px; text-transform: uppercase; }
  .contact__role { top: 90px; font-size: 17px; font-weight: 300; font-style: italic; text-transform: uppercase; letter-spacing: 1.2px; }
  .contact__email { top: 115px; font-size: 16.5px; font-weight: 300; letter-spacing: 0.2px; }

  .phone { position: absolute; left: 52px; display: flex; align-items: center; gap: 10px; font-family: "Montserrat", sans-serif; font-weight: 300; font-size: 19px; letter-spacing: 0.6px; color: var(--ink); line-height: 1; }
  .phone--office { top: 172px; }
  .phone--cell { top: 203px; }
  .phone svg { width: 24px; height: 26px; flex: none; }

  .contact__licence { top: 279px; font-size: 17px; font-weight: 300; text-transform: uppercase; letter-spacing: 1.3px; }
  .contact__address { top: 301px; font-size: 17px; font-weight: 300; text-transform: uppercase; letter-spacing: 1.3px; }

  .web-band {
    position: absolute; left: 0; right: 0; top: 363px; height: 60px;
    background: linear-gradient(90deg, var(--yellow) 0%, var(--orange-mid) 40%, var(--orange-deep) 100%);
    display: flex; align-items: center; justify-content: center;
    font-family: "Montserrat", sans-serif; font-weight: 300; font-size: 17px;
    color: var(--paper); letter-spacing: 0.8px;
  }
</style>
</head>
<body>
<div class="sheet">

  <section class="card card--front" aria-label="Card front">
    <div class="front-panel">
      <span class="brand-dot" aria-hidden="true"></span>
      <span class="brand-name">corvane</span>
    </div>
  </section>

  <section class="card card--back" aria-label="Card back">
    <p class="contact contact__name">Walter Brindley</p>
    <p class="contact contact__role">Home Comfort Consultant</p>
    <p class="contact contact__email">walter@corvane-hvac.example</p>

    <p class="phone phone--office">
      <svg viewBox="0 0 24 24" aria-hidden="true"><path d="M6.5 2.5 L9.5 6.5 L7.8 8.6 C9 11.3 12.2 14.6 15 15.8 L17.2 14 L21.3 17 L19.8 19.8 C18.9 21.2 17 21.4 15.4 20.6 C9.7 18 5.6 13.7 3.2 8.4 C2.5 6.9 2.7 5 4 4 Z" fill="none" stroke="#f47f20" stroke-width="1.6" stroke-linejoin="round"/></svg>
      888-731-5096
    </p>
    <p class="phone phone--cell">
      <svg viewBox="0 0 24 26" aria-hidden="true"><rect x="6" y="1.5" width="12" height="23" rx="2" fill="none" stroke="#f47f20" stroke-width="1.6"/><line x1="6" y1="5.5" x2="18" y2="5.5" stroke="#f47f20" stroke-width="1.4"/><line x1="6" y1="20" x2="18" y2="20" stroke="#f47f20" stroke-width="1.4"/><circle cx="12" cy="22.3" r="0.9" fill="#f47f20"/></svg>
      510-842-3917
    </p>

    <p class="contact contact__licence">Lic.# 583164</p>
    <p class="contact contact__address">4827 Moravia Ct #215 Oakland, CA 94602</p>

    <div class="web-band">www.corvane-hvac.example</div>
  </section>

</div>
</body>
</html>
```